Landing Page and Logo for Auto-Blogging Platform

I created a platform that allows users to start a blog for their business, hobby, charity, etc. I need a landing page where users can learn about the platform, benefits of consistent blogging, SEO value, plans/pricing, etc. The landing page needs to have multiple call to action buttons encouraging the visitor to register/sign up for a free trial.

In addition to the landing page, I need a page for users to establish the settings for their blog. This page should be a fairly simple form, intended for the user to enter a few details to set up their blog:
1. Name of Blog
2. Up to 10 topics and/or keywords the blog should focus on
3. Theme: Color-scheme and logo upload for blog.

I have attached the specifications of the platform's functionality so you can better understand how it works, plans/pricing, etc.

I also need a logo for the business. The name of the platform is PennaWave.

Target Market(s)

Website owners, bloggers, business owners

Industry/Entity Type

Technology, Internet, web design

Coding

Coded - Design and coding required

Number of Pages Required

2 page

Colors
0054AA
0677BA
7BADD7
CADEEF
E8F1F8
0094D4
00A9DD
6FCCEA
C7EBF8
E9F6FB

Requirements
Must have
• Eye-catching design but fairly light on content (keep it simple and brief.)
Nice to have
• Eye-catching yet simple design, clean and easy to understand what we are offering.
Should not have
• Too much “wordy” and confusing content.

```html
<!DOCTYPE html>
<html lang="en">
<head>
<meta charset="utf-8">
<title>PennaWave – Auto-Blogging Platform</title>
<link href="https://fonts.googleapis.com/css2?family=Poppins:wght@400;500;600;700&display=swap" rel="stylesheet">
<style>
:root{
  --blue-deep:#0054AA;
  --blue:#0677BA;
  --blue-mid:#7BADD7;
  --blue-pale:#CADEEF;
  --blue-wash:#E8F1F8;
  --sky:#0094D4;
  --sky-bright:#00A9DD;
  --sky-soft:#6FCCEA;
  --sky-pale:#C7EBF8;
  --sky-wash:#E9F6FB;
  --ink:#1d1d1f;
  --text:#3a3a3a;
  --navy:#0b2d5e;
  --star:#f5b82e;
  --white:#fff;
}
*{margin:0;padding:0;box-sizing:border-box}
html,body{width:1200px;height:4252px;overflow:hidden}
body{font-family:'Poppins',sans-serif;color:var(--text);background:var(--white)}
.section{position:relative;width:1200px;overflow:hidden}
.abs{position:absolute}
.btn{position:absolute;display:flex;align-items:center;justify-content:center;font-size:14px;font-weight:600;height:41px;padding:0 22px;text-decoration:none}
.btn--solid{background:var(--blue-deep);color:var(--white)}
.btn--light{background:var(--white);color:var(--ink)}
.heading{font-size:30px;font-weight:700;color:var(--ink);line-height:1.25}
.heading-rule{width:56px;height:3px;background:var(--sky);margin-top:12px}
.art{position:absolute;border-radius:14px}

/* hero */
.hero{height:670px;background:radial-gradient(ellipse at 80% 20%,#1566c0 0%,var(--blue-deep) 55%,#0a4c9c 100%)}
.brand{left:143px;top:30px;color:var(--white);font-size:30px;font-weight:600;letter-spacing:1px}
.hero__title{left:143px;top:238px;width:470px;color:var(--white);font-size:31px;font-weight:700;line-height:46px}
.hero .art{left:640px;top:157px;width:416px;height:421px;background:linear-gradient(160deg,#3d8fd6,#2a6fbd 60%,#f0b43c22)}

/* about */
.about{height:604px}
.about .art{left:143px;top:90px;width:437px;height:425px;background:linear-gradient(150deg,var(--blue-wash),var(--sky-pale) 60%,#fde3b0)}
.about__body{left:643px;top:130px;width:405px}
.about__text{margin-top:48px;font-size:12.6px;line-height:19.2px}

/* how it works */
.how{height:766px;background:var(--sky-wash)}
.how__title{left:0;top:78px;width:1200px;text-align:center}
.how__intro{left:300px;top:166px;width:600px;text-align:center;font-size:12.6px;line-height:19px}
.step{position:absolute;width:200px;text-align:center}
.step__icon{width:92px;height:92px;margin:0 auto;border-radius:50%;background:var(--white);box-shadow:0 4px 14px rgba(0,84,170,.14);display:flex;align-items:center;justify-content:center}
.step__icon span{display:block;width:48px;height:48px;border-radius:10px;background:linear-gradient(140deg,var(--blue-pale),var(--sky-soft))}
.step__label{margin-top:18px;font-size:18.5px;font-weight:600;color:var(--ink);line-height:27px}

/* lists with ticks */
.checks{position:absolute;list-style:none}
.checks li{display:flex;align-items:center;height:34px;font-size:12.6px;font-weight:500;color:var(--ink)}
.checks svg{width:14px;height:14px;margin-right:13px;flex:none}

/* benefits */
.benefits{height:564px}
.benefits__title{left:143px;top:90px;width:400px}
.benefits .art{left:640px;top:88px;width:416px;height:400px;background:linear-gradient(170deg,var(--white),var(--blue-wash) 40%,#fbe0a6 75%,var(--blue-pale))}

/* seo */
.seo{height:553px;background:var(--sky-wash)}
.seo .art{left:143px;top:77px;width:418px;height:388px;background:linear-gradient(150deg,var(--white),var(--blue-pale) 55%,#fcdca0)}
.seo__title{left:642px;top:112px}

/* pricing */
.pricing{height:600px;background:radial-gradient(ellipse at 15% 90%,#1566c0 0%,var(--blue-deep) 55%,#0a4c9c 100%)}
.pricing__title{left:0;top:66px;width:1200px;text-align:center;color:var(--white);font-size:32px;font-weight:700}
.pricing__intro{left:285px;top:160px;width:630px;text-align:center;color:var(--white);font-size:12.6px;line-height:19px}
.plans{position:absolute;left:272px;top:230px;width:655px;border-collapse:collapse;table-layout:fixed}
.plans th{height:37px;background:var(--sky);color:var(--white);font-size:17px;font-weight:600;border-right:1px solid #3fb3e2}
.plans td{height:160px;background:var(--sky-wash);text-align:center;vertical-align:top;padding-top:22px;font-size:12.6px;line-height:19px;color:var(--ink);border-right:1px solid var(--blue-pale)}
.plans th:last-child,.plans td:last-child{border-right:0}
.price{display:block;margin-top:6px;color:var(--sky);font-size:22px;font-weight:700}
.price small{font-size:12px;font-weight:500}

/* testimonials */
.reviews{height:456px}
.reviews__title{left:0;top:80px;width:1200px;text-align:center}
.card{position:absolute;top:150px;width:288px;height:218px;background:var(--sky-wash);border-radius:10px;padding:28px 28px 0}
.stars{color:var(--star);font-size:14px;letter-spacing:3px}
.card__text{margin-top:12px;font-size:12.4px;line-height:19px;color:var(--text)}
.card__who{position:absolute;left:28px;bottom:24px;display:flex;align-items:center;gap:14px;font-size:14px;font-weight:600;color:var(--ink)}
.avatar{width:40px;height:40px;border-radius:50%;background:linear-gradient(150deg,#b98a6a,#6e4a36)}
.quote{position:absolute;right:28px;bottom:4px;font-size:78px;font-weight:700;line-height:1;color:var(--sky);font-family:Georgia,serif}
.arrow{position:absolute;top:242px;width:36px;height:36px;border-radius:50%;display:flex;align-items:center;justify-content:center}
.arrow--prev{left:76px;background:var(--blue-wash)}
.arrow--next{left:1088px;background:var(--blue-deep)}

.footer{height:39px;background:var(--navy);color:var(--white);font-size:12px;display:flex;align-items:center;justify-content:center}
</style>
</head>
<body>

<header class="section hero">
  <div class="abs brand">PENNAWAVE</div>
  <a class="btn btn--light" style="left:950px;top:28px;height:42px;width:108px" href="#">Sign Up</a>
  <h1 class="abs hero__title">Share Your Voice And Connect With Like-minded Writers. Explore, Create, And Grow On Our Blogging Portal.</h1>
  <a class="btn btn--light" style="left:143px;top:450px;width:209px" href="#">Sign Up For A Free Trial</a>
  <div class="art" role="img" aria-label="Isometric illustration of a writer at a desk surrounded by floating blog, chart and media panels"></div>
</header>

<section class="section about">
  <div class="art" role="img" aria-label="Illustration of a woman with a laptop in front of a large web page layout"></div>
  <div class="abs about__body">
    <h2 class="heading">About The Platform</h2>
    <div class="heading-rule"></div>
    <p class="about__text">Lorem Ipsum is simply dummy text of the printing and typesetting industry. Lorem Ipsum has been the industry's standard dummy text ever since the 1500s, when an unknown printer took a galley of type and scrambled it to make a type specimen book. It has survived not only five centuries, but also the leap into electronic typesetting, remaining essentially unchanged. It was popularised in the 1960s with the release of Transfer sheets containing Lorem Ipsum passages, and more recently with desktop publishing software like Layout Studio including versions of Lorem Ipsum.</p>
  </div>
  <a class="btn btn--solid" style="left:643px;top:432px;width:212px" href="#">Sign Up For A Free Trial</a>
</section>

<section class="section how">
  <h2 class="abs heading how__title">How It Work</h2>
  <p class="abs how__intro">The purpose of this platform is to allow anyone to start a blog and automate the process of creating content and posting it to the blog. Here is what the platform will consist of.</p>
  <div class="step" style="left:86px;top:239px"><div class="step__icon" role="img" aria-label="User login icon"><span></span></div><div class="step__label">Log in</div></div>
  <div class="step" style="left:337px;top:239px"><div class="step__icon" role="img" aria-label="Writing on laptop icon"><span></span></div><div class="step__label">Create a new<br>blog post</div></div>
  <div class="step" style="left:624px;top:239px"><div class="step__icon" role="img" aria-label="Document layout icon"><span></span></div><div class="step__label">Format and<br>optimize</div></div>
  <div class="step" style="left:911px;top:239px"><div class="step__icon" role="img" aria-label="Sending post icon"><span></span></div><div class="step__label">Publish or<br>schedule</div></div>
  <div class="step" style="left:210px;top:439px"><div class="step__icon" role="img" aria-label="Reader interaction icon"><span></span></div><div class="step__label">Engage with<br>readers</div></div>
  <div class="step" style="left:497px;top:439px"><div class="step__icon" role="img" aria-label="Analytics dashboard icon"><span></span></div><div class="step__label">Monitor<br>performance</div></div>
  <div class="step" style="left:783px;top:439px"><div class="step__icon" role="img" aria-label="Improvement cycle icon"><span></span></div><div class="step__label">Adjust and<br>improve</div></div>
  <a class="btn btn--solid" style="left:495px;top:638px;width:210px" href="#">Sign Up For A Free Trial</a>
</section>

<section class="section benefits">
  <h2 class="abs heading benefits__title">Benefits Of Consistent Blogging</h2>
  <div class="abs heading-rule" style="left:143px;top:168px;margin:0"></div>
  <ul class="checks" style="left:143px;top:202px">
    <li><svg viewBox="0 0 14 14"><circle cx="7" cy="7" r="6" fill="none" stroke="#0094D4" stroke-width="1.4"/><path d="M4 7.2l2 2 4-4.2" fill="none" stroke="#0094D4" stroke-width="1.5"/></svg>Improved SEO</li>
    <li><svg viewBox="0 0 14 14"><circle cx="7" cy="7" r="6" fill="none" stroke="#0094D4" stroke-width="1.4"/><path d="M4 7.2l2 2 4-4.2" fill="none" stroke="#0094D4" stroke-width="1.5"/></svg>Increased Authority</li>
    <li><svg viewBox="0 0 14 14"><circle cx="7" cy="7" r="6" fill="none" stroke="#0094D4" stroke-width="1.4"/><path d="M4 7.2l2 2 4-4.2" fill="none" stroke="#0094D4" stroke-width="1.5"/></svg>Enhanced Engagement</li>
    <li><svg viewBox="0 0 14 14"><circle cx="7" cy="7" r="6" fill="none" stroke="#0094D4" stroke-width="1.4"/><path d="M4 7.2l2 2 4-4.2" fill="none" stroke="#0094D4" stroke-width="1.5"/></svg>Content Variety</li>
    <li><svg viewBox="0 0 14 14"><circle cx="7" cy="7" r="6" fill="none" stroke="#0094D4" stroke-width="1.4"/><path d="M4 7.2l2 2 4-4.2" fill="none" stroke="#0094D4" stroke-width="1.5"/></svg>Higher Conversion Rates</li>
  </ul>
  <ul class="checks" style="left:352px;top:202px">
    <li><svg viewBox="0 0 14 14"><circle cx="7" cy="7" r="6" fill="none" stroke="#0094D4" stroke-width="1.4"/><path d="M4 7.2l2 2 4-4.2" fill="none" stroke="#0094D4" stroke-width="1.5"/></svg>Brand Visibility</li>
    <li><svg viewBox="0 0 14 14"><circle cx="7" cy="7" r="6" fill="none" stroke="#0094D4" stroke-width="1.4"/><path d="M4 7.2l2 2 4-4.2" fill="none" stroke="#0094D4" stroke-width="1.5"/></svg>Audience Insights</li>
    <li><svg viewBox="0 0 14 14"><circle cx="7" cy="7" r="6" fill="none" stroke="#0094D4" stroke-width="1.4"/><path d="M4 7.2l2 2 4-4.2" fill="none" stroke="#0094D4" stroke-width="1.5"/></svg>Enhanced Social Media Presence</li>
    <li><svg viewBox="0 0 14 14"><circle cx="7" cy="7" r="6" fill="none" stroke="#0094D4" stroke-width="1.4"/><path d="M4 7.2l2 2 4-4.2" fill="none" stroke="#0094D4" stroke-width="1.5"/></svg>Networking Opportunities</li>
    <li><svg viewBox="0 0 14 14"><circle cx="7" cy="7" r="6" fill="none" stroke="#0094D4" stroke-width="1.4"/><path d="M4 7.2l2 2 4-4.2" fill="none" stroke="#0094D4" stroke-width="1.5"/></svg>Long-Term Benefits</li>
  </ul>
  <a class="btn btn--solid" style="left:143px;top:435px;width:210px" href="#">Sign Up For A Free Trial</a>
  <div class="art" role="img" aria-label="Illustration of a man with a briefcase climbing rising bar chart steps"></div>
</section>

<section class="section seo">
  <div class="art" role="img" aria-label="Illustration of a person with a tablet beside a search screen, rocket and globe"></div>
  <div class="abs seo__title"><h2 class="heading">SEO Value</h2><div class="heading-rule"></div></div>
  <ul class="checks" style="left:642px;top:184px">
    <li><svg viewBox="0 0 14 14"><circle cx="7" cy="7" r="6" fill="none" stroke="#0094D4" stroke-width="1.4"/><path d="M4 7.2l2 2 4-4.2" fill="none" stroke="#0094D4" stroke-width="1.5"/></svg>Fresh Content</li>
    <li><svg viewBox="0 0 14 14"><circle cx="7" cy="7" r="6" fill="none" stroke="#0094D4" stroke-width="1.4"/><path d="M4 7.2l2 2 4-4.2" fill="none" stroke="#0094D4" stroke-width="1.5"/></svg>Keyword Optimization</li>
    <li><svg viewBox="0 0 14 14"><circle cx="7" cy="7" r="6" fill="none" stroke="#0094D4" stroke-width="1.4"/><path d="M4 7.2l2 2 4-4.2" fill="none" stroke="#0094D4" stroke-width="1.5"/></svg>Increased Indexing</li>
    <li><svg viewBox="0 0 14 14"><circle cx="7" cy="7" r="6" fill="none" stroke="#0094D4" stroke-width="1.4"/><path d="M4 7.2l2 2 4-4.2" fill="none" stroke="#0094D4" stroke-width="1.5"/></svg>Internal Linking</li>
    <li><svg viewBox="0 0 14 14"><circle cx="7" cy="7" r="6" fill="none" stroke="#0094D4" stroke-width="1.4"/><path d="M4 7.2l2 2 4-4.2" fill="none" stroke="#0094D4" stroke-width="1.5"/></svg>Backlink Opportunities</li>
  </ul>
  <ul class="checks" style="left:858px;top:184px">
    <li><svg viewBox="0 0 14 14"><circle cx="7" cy="7" r="6" fill="none" stroke="#0094D4" stroke-width="1.4"/><path d="M4 7.2l2 2 4-4.2" fill="none" stroke="#0094D4" stroke-width="1.5"/></svg>Engagement Metrics</li>
    <li><svg viewBox="0 0 14 14"><circle cx="7" cy="7" r="6" fill="none" stroke="#0094D4" stroke-width="1.4"/><path d="M4 7.2l2 2 4-4.2" fill="none" stroke="#0094D4" stroke-width="1.5"/></svg>Long-Tail Keywords</li>
    <li><svg viewBox="0 0 14 14"><circle cx="7" cy="7" r="6" fill="none" stroke="#0094D4" stroke-width="1.4"/><path d="M4 7.2l2 2 4-4.2" fill="none" stroke="#0094D4" stroke-width="1.5"/></svg>Local SEO Benefits</li>
    <li><svg viewBox="0 0 14 14"><circle cx="7" cy="7" r="6" fill="none" stroke="#0094D4" stroke-width="1.4"/><path d="M4 7.2l2 2 4-4.2" fill="none" stroke="#0094D4" stroke-width="1.5"/></svg>Enhanced User Experience</li>
    <li><svg viewBox="0 0 14 14"><circle cx="7" cy="7" r="6" fill="none" stroke="#0094D4" stroke-width="1.4"/><path d="M4 7.2l2 2 4-4.2" fill="none" stroke="#0094D4" stroke-width="1.5"/></svg>Authority Building</li>
  </ul>
  <a class="btn btn--solid" style="left:642px;top:387px;width:211px" href="#">Sign Up For A Free Trial</a>
</section>

<section class="section pricing">
  <h2 class="abs pricing__title">Pricing</h2>
  <div class="abs heading-rule" style="left:572px;top:118px;margin:0"></div>
  <p class="abs pricing__intro">The platform can be used to sell unique accounts to multiple users. There must be a subscription plan and a 14-day free trial. The subscriptions are:</p>
  <table class="plans">
    <tr><th>Base Plan</th><th>Premium Plan</th><th>Ultimate Plan</th></tr>
    <tr>
      <td>1 blog post<br>(up to 2,000 words)<br>every month<span class="price">$9.99/<small>mo.</small></span></td>
      <td>1 blog post<br>(up to 2,000 words)<br>every week<span class="price">$14.99/<small>mo.</small></span></td>
      <td>1 blog post<br>(up to 3,000 words)<br>per day plus unlimited<br>manual posting<span class="price">$24.99/<small>mo.</small></span></td>
    </tr>
  </table>
  <a class="btn btn--light" style="left:495px;top:471px;width:210px;color:var(--blue-deep)" href="#">Sign Up For A Free Trial</a>
</section>

<section class="section reviews">
  <h2 class="abs heading reviews__title">Let’s See Our Customer Say</h2>
  <div class="arrow arrow--prev"><svg width="12" height="12" viewBox="0 0 12 12"><path d="M8 1L3 6l5 5" fill="none" stroke="#0054AA" stroke-width="2"/></svg></div>
  <article class="card" style="left:142px">
    <div class="stars">★★★★★</div>
    <p class="card__text">Lorem ipsum dolor sit amet, consectetur adipiscing elit. Proin suscipit metus tellus, at ultricies libero pulvinar sit amet.</p>
    <div class="card__who"><div class="avatar" role="img" aria-label="Customer portrait"></div>Milo Harrant</div>
    <div class="quote">”</div>
  </article>
  <article class="card" style="left:455px">
    <div class="stars">★★★★★</div>
    <p class="card__text">Lorem ipsum dolor sit amet, consectetur adipiscing elit. Proin suscipit metus tellus, at ultricies libero pulvinar sit amet.</p>
    <div class="card__who"><div class="avatar" role="img" aria-label="Customer portrait"></div>Rena Colby</div>
    <div class="quote">”</div>
  </article>
  <article class="card" style="left:769px">
    <div class="stars">★★★★★</div>
    <p class="card__text">Lorem ipsum dolor sit amet, consectetur adipiscing elit. Proin suscipit metus tellus, at ultricies libero pulvinar sit amet.</p>
    <div class="card__who"><div class="avatar" role="img" aria-label="Customer portrait"></div>Jonas Verel</div>
    <div class="quote">”</div>
  </article>
  <div class="arrow arrow--next"><svg width="12" height="12" viewBox="0 0 12 12"><path d="M4 1l5 5-5 5" fill="none" stroke="#fff" stroke-width="2"/></svg></div>
</section>

<footer class="section footer">© 2024 PennaWave. All Rights Reserved.</footer>

</body>
</html>
```